Business Card for By Karel Voss

Looking to have a business card designed for my lifestyle and fitness company. My company offers personal training, online programming and nutrition advice based out of London, United Kingdom.

I'd like to see modern, sleek designs, focusing on black, matte black or matte grey. Design doesn't need to be overly descriptive as this will also be used as a personal business card. I've included my logo.

Please note that my company is no longer called "By Karel Voss" but instead "By Karel Voss", this is because of my other ventures. Therefore please don't use the "fitness by karel voss" text.

information about my company can be found at www.bykarelvoss.com

Company is also based out of London (United Kingdom) & Sydney (Australia) this could be reflected on the card.

Industry/Entity Type

Business

Contact Information for Business Card

Karel Voss
+44 7382 615027
karel@bykarelvoss.com
www.bykarelvoss.com

Font styles to use
Sans Serif

Requirements
Must have
• All contact details and inclusion of my logo.

```html
<!DOCTYPE html>
<html lang="en">
<head>
<meta charset="utf-8">
<title>By Karel Voss — Business Card</title>
<link rel="stylesheet" href="https://fonts.googleapis.com/css2?family=Oswald:wght@500&family=Roboto:wght@400;700&display=swap">
<style>
  :root {
    --backdrop: #4a443d;
    --card: #231f20;
    --ink: #ffffff;
    --ink-soft: #e6e6e6;
    --rule: #bfbfbf;
  }
  * { margin: 0; padding: 0; box-sizing: border-box; }
  html, body { width: 1200px; height: 930px; overflow: hidden; }
  body {
    position: relative;
    background: var(--backdrop);
    font-family: "Roboto", Arial, sans-serif;
    color: var(--ink);
  }
  .card {
    position: absolute;
    width: 560px;
    height: 320px;
    background: var(--card);
    border-radius: 14px;
    box-shadow: 0 6px 18px rgba(0,0,0,.35);
  }
  .card--front { left: 110px; top: 90px; }
  .card--back  { left: 530px; top: 500px; }

  .brand {
    display: flex;
    align-items: center;
    gap: 10px;
    font-family: "Roboto", Arial, sans-serif;
    font-weight: 700;
    text-transform: uppercase;
    letter-spacing: 1px;
    color: var(--ink);
  }
  .brand__mark {
    background: var(--ink);
    flex: none;
  }
  .card--front .brand {
    position: absolute;
    left: 0; right: 0; top: 140px;
    justify-content: center;
    font-size: 26px;
  }
  .card--front .brand__mark { width: 22px; height: 22px; }

  .card--back .brand {
    position: absolute;
    left: 36px; top: 44px;
    font-size: 17px;
  }
  .card--back .brand__mark { width: 16px; height: 16px; }

  .top-rule {
    position: absolute;
    left: 240px; right: 34px; top: 54px;
    height: 1px;
    background: var(--rule);
  }
  .holder {
    position: absolute;
    left: 36px; top: 170px;
    right: 34px;
  }
  .holder__name {
    font-family: "Oswald", "Arial Narrow", sans-serif;
    font-weight: 500;
    font-size: 30px;
    letter-spacing: 1.5px;
    text-transform: uppercase;
    line-height: 1;
  }
  .holder__role {
    display: flex;
    align-items: center;
    gap: 8px;
    margin-top: 6px;
    font-size: 13px;
    color: var(--ink-soft);
  }
  .holder__role::after {
    content: "";
    flex: 1;
    height: 1px;
    background: var(--rule);
  }
  .contact {
    position: absolute;
    left: 36px; top: 240px;
    list-style: none;
    font-size: 14px;
    color: var(--ink-soft);
  }
  .contact li {
    display: flex;
    align-items: center;
    gap: 10px;
    height: 22px;
  }
  .contact svg { width: 11px; height: 11px; fill: none; stroke: var(--ink-soft); stroke-width: 1.6; }
</style>
</head>
<body>
  <section class="card card--front" aria-label="Card front">
    <div class="brand"><span class="brand__mark"></span>By Karel Voss</div>
  </section>

  <section class="card card--back" aria-label="Card back">
    <div class="brand"><span class="brand__mark"></span>By Karel Voss</div>
    <div class="top-rule"></div>

    <div class="holder">
      <h1 class="holder__name">Karel Voss</h1>
      <p class="holder__role">Trainer</p>
    </div>

    <ul class="contact">
      <li>
        <svg viewBox="0 0 12 12" aria-hidden="true"><path d="M3 1 L5 3.5 L4 5 Q5.5 7 7 8 L8.5 7 L11 9 L9.5 11 Q5 10 1 3 Z"/></svg>
        +44 7382 615027
      </li>
      <li>
        <svg viewBox="0 0 12 12" aria-hidden="true"><rect x="1" y="2.5" width="10" height="7"/><path d="M1 2.5 L6 6.5 L11 2.5"/></svg>
        karel@bykarelvoss.com
      </li>
      <li>
        <svg viewBox="0 0 12 12" aria-hidden="true"><circle cx="6" cy="6" r="5"/><path d="M1 6 H11 M6 1 Q3 6 6 11 Q9 6 6 1"/></svg>
        www.bykarelvoss.com
      </li>
    </ul>
  </section>
</body>
</html>
```